Travolex - Clever Border Flow Shaping Enterprises

Web Design for international start-up, which is automating customs clearance processes for forwarding companies by applying a web application, which is operating with artificial intelligence and robotic process automation. Travolex pursues the vision of supporting forwarding companies successfully in becoming digital masters and co-creates innovative software solutions with all participants (ex- and importers of goods) along value-added chains. With intelligent/smart/digital customs clearance software or in other words, a virtual customs clearance roboter tailord to the customers needs, we are transforming businesses. The website could look like this:

https://www.kelvora.com/uk-en/index.php
or
https://pagebuildly.com/theme/marrowgate

Please use colours and designs you think would be the best fit. These websites are just here to give you an idea of how the webdesign could look like. Use the attached logo design as a basis for further web design. You can use the provided pictures, but you can also use your own ones, if you think they are better suited. But please take care, that they have a high resolution quality.

Description of Website: The website is transparent and modern. It provides seven pages such as homepage, products, web app, the about us, working at Travolex, News, contact us and search results page. The homepage or landing page should be filled with a short description of the company, what Travolex is doing, how they will support its customers and will also include a video of the provided solution. Products provide obviously information about different products and their characteristics. Web app page includes information about principles and technologies that get the software going. The about us page includes unique advantages and value propositions for customers and the contact us, as the name already says, will provide contact information and possibilities to contact us. The rest is also obvious (for additional information look up the website of KLV, priorly provided link - the page is also available in english).

If you have any questions, I am happy to answer them any time.
Updates

I have to think about the text that I want to have included into the design and hadn't have the time to compose it.

Target Market(s)

Forwarding Companies, Ex-/Importers

Industry/Entity Type

It Company

Number of Pages Required

5+ page

Requirements
Must have
• The web design should be designes according to the attached logo of Travolex.

```html
<!DOCTYPE html>
<html lang="en">
<head>
<meta charset="utf-8">
<title>Travolex - Clever Border Flow Shaping Enterprises</title>
<link href="https://fonts.googleapis.com/css2?family=Poppins:wght@300;400;500;600;700&display=swap" rel="stylesheet">
<style>
:root{
  --blue:#1f7fd4;
  --blue-deep:#2a5fc4;
  --teal:#26b8dc;
  --ink:#1f2b3a;
  --muted:#7b8694;
  --line:#e4e9ef;
  --paper:#ffffff;
  --soft:#f4f7fa;
}
*{box-sizing:border-box;margin:0;padding:0}
html,body{width:1200px;height:3930px;overflow:hidden}
body{font-family:'Poppins',sans-serif;color:var(--ink);background:var(--paper);position:relative}
section,header,footer{position:absolute;left:0;width:1200px}
.brand{display:flex;align-items:center;gap:10px}
.brand-dot{width:30px;height:30px;border-radius:50%;background:var(--teal)}
.brand-name{font-size:34px;font-weight:600;color:var(--blue);line-height:1}
.brand-tag{font-size:9px;color:var(--muted);margin-top:2px}

/* header */
.site-header{top:0;height:105px;background:#fff;border-top:10px solid var(--teal)}
.site-header .brand{position:absolute;left:55px;top:28px}
.nav{position:absolute;left:335px;top:40px;display:flex;gap:30px;font-size:13px;color:var(--ink)}
.nav .active{color:var(--blue);border-bottom:2px solid var(--blue);padding-bottom:8px}
.btn-contact{position:absolute;right:55px;top:30px;width:122px;height:40px;border:2px solid var(--teal);border-radius:20px;font-size:13px;font-weight:500;display:flex;align-items:center;justify-content:center}

/* hero */
.hero{top:105px;height:635px;background:linear-gradient(120deg,var(--blue-deep) 0%,#2f8fdc 55%,var(--teal) 100%);color:#fff;overflow:hidden}
.hero h1{position:absolute;left:55px;top:150px;font-size:56px;line-height:62px;font-weight:700}
.hero h1 span{font-weight:300}
.hero p{position:absolute;left:55px;top:315px;width:540px;font-size:13.5px;line-height:22px;opacity:.92}
.hero p::before{content:"";position:absolute;left:0;top:-20px;width:60px;height:2px;background:#fff}
.search{position:absolute;left:55px;top:415px;width:405px;height:48px;background:#fff;border-radius:24px;border:3px solid rgba(255,255,255,.5)}
.search span{position:absolute;left:22px;top:13px;font-size:12px;color:#9aa4ae}
.search b{position:absolute;right:0;top:0;width:145px;height:42px;border-radius:21px;background:var(--blue);font-size:13px;font-weight:500;display:flex;align-items:center;justify-content:center;color:#fff}
.hero-art{position:absolute;left:560px;top:90px;width:580px;height:510px;background:radial-gradient(ellipse at 60% 50%,rgba(255,255,255,.55) 0%,rgba(190,230,250,.35) 35%,rgba(31,127,212,.15) 60%,rgba(31,127,212,0) 75%)}
.notch{position:absolute;left:565px;width:70px;height:34px;border-radius:0 0 35px 35px}

/* heading */
.sec-head{position:absolute;left:0;width:1200px;text-align:center}
.sec-head i{display:block;width:30px;height:30px;margin:0 auto 10px;border-radius:50%;background:var(--teal)}
.sec-head h2{font-size:30px;font-weight:400}
.sec-head h2 b{font-weight:600}

/* products */
.products{top:740px;height:415px;background:linear-gradient(180deg,#fff,var(--soft))}
.prod-row{position:absolute;left:418px;top:180px;display:flex;gap:22px}
.prod{width:110px;height:165px;border-radius:55px;background:linear-gradient(180deg,var(--teal),var(--blue));border:5px solid #fff;box-shadow:0 0 0 3px var(--blue);color:#fff;font-size:13px;font-weight:600;text-align:center;display:flex;flex-direction:column;align-items:center;justify-content:center;line-height:16px;gap:10px}
.prod svg{width:40px;height:40px}

/* about */
.about{top:1155px;height:405px;background:linear-gradient(100deg,#2d6fc6,var(--blue) 50%,#3296d8);color:#fff}
.about-photo{position:absolute;left:150px;top:70px;width:260px;height:260px;border-radius:50%;border:10px solid rgba(255,255,255,.35);background:linear-gradient(135deg,#1e2e45 0%,#45607e 45%,#b9c8d6 80%,#e6ecf1 100%)}
.about .sec-head{left:485px;width:auto;top:32px;text-align:left;display:flex;align-items:center;gap:10px}
.about .sec-head i{margin:0;background:#fff}
.about .text{position:absolute;left:525px;top:80px;width:510px;font-size:12.5px;line-height:20px;opacity:.92}
.about .text p+p{margin-top:14px}
.btn-more{position:absolute;height:32px;width:135px;border-radius:16px;background:linear-gradient(90deg,var(--blue),var(--teal));color:#fff;font-size:12px;font-weight:500;display:flex;align-items:center;justify-content:center}

/* web app */
.webapp{top:1560px;height:785px;background:#fff}
.lead{position:absolute;left:220px;top:185px;width:760px;text-align:center;font-size:20px;line-height:34px;color:#4b5563;font-weight:300}
.webapp-art{position:absolute;left:150px;top:285px;width:280px;height:280px;border-radius:50%;background:linear-gradient(135deg,var(--blue),var(--teal))}
.webapp-photo{position:absolute;left:180px;top:300px;width:230px;height:230px;border-radius:50%;background:linear-gradient(140deg,#e9eef3 0%,#b6c3cf 40%,#5b6c7e 75%,#2b3848 100%);border:6px solid #fff}
.quote{position:absolute;left:480px;top:315px;width:540px;font-size:13px;line-height:22px;color:var(--muted)}
.quote p+p{margin-top:20px}
.strip{position:absolute;left:0;top:600px;width:1200px;height:95px;background:linear-gradient(90deg,#fff,#e9f7fb 50%,#fff);text-align:center;font-size:14px;font-style:italic;color:var(--ink);padding-top:20px}
.strip b{display:block;font-style:normal;color:var(--blue);font-size:13px;margin-top:4px;font-weight:500}

/* how it works */
.how{top:2345px;height:405px;background:linear-gradient(110deg,#2d6cc4,var(--blue) 55%,var(--teal));color:#fff}
.how .frame{position:absolute;left:100px;top:38px;width:490px;height:290px;border:2px dashed rgba(255,255,255,.45);border-right:none;border-bottom:none;border-radius:30px 0 0 0}
.how .sec-head{left:145px;top:50px;width:auto;text-align:left;display:flex;align-items:center;gap:10px}
.how .sec-head i{margin:0;background:#fff}
.how .text{position:absolute;left:150px;top:112px;width:440px;font-size:13px;line-height:22px}
.how .text p+p{margin-top:16px}
.video{position:absolute;left:635px;top:55px;width:450px;height:300px;background:linear-gradient(180deg,#3e4752 0%,#7d6e5c 45%,#b59d7f 70%,#5a5149 100%)}
.play{position:absolute;left:195px;top:120px;width:60px;height:60px;border-radius:50%;background:rgba(255,255,255,.92)}
.play::after{content:"";position:absolute;left:24px;top:18px;border-left:18px solid var(--blue);border-top:12px solid transparent;border-bottom:12px solid transparent}

/* news */
.news{top:2750px;height:600px;background:#fff}
.cards{position:absolute;left:170px;top:170px;display:flex;gap:35px}
.card{width:265px;height:355px;background:#fff;box-shadow:0 4px 18px rgba(0,0,0,.08);text-align:center;position:relative}
.card .ph{height:165px;margin:10px;position:relative}
.ph-a{background:linear-gradient(135deg,#1d2a38,#4d6178 55%,#9fb0c1)}
.ph-b{background:linear-gradient(135deg,#f1d57a,#e79a4c 45%,#7a6a5d 80%,#d9d2c4)}
.ph-c{background:linear-gradient(135deg,#16324f,#2f5f8c 50%,#8eb1cf)}
.card .date{position:absolute;left:0;bottom:0;background:rgba(20,30,40,.75);color:#fff;font-size:9px;padding:3px 8px}
.card h3{font-size:17px;font-weight:400;margin-top:6px}
.card .meta{font-size:9px;color:var(--blue);margin:6px 0 10px}
.card p{font-size:11px;line-height:18px;color:var(--muted);padding:0 25px}
.card a{display:block;font-size:11px;color:var(--blue);font-weight:600;margin-top:4px}

/* map */
.map{top:3350px;height:230px;background:linear-gradient(160deg,#eceef0 0%,#dfe3e6 40%,#e7eaec 70%,#d4d9dd 100%)}

/* footer */
.site-footer{top:3580px;height:300px;background:#f7f8fa}
.site-footer .brand{position:absolute;left:150px;top:30px}
.f-about{position:absolute;left:150px;top:105px;width:300px;font-size:12px;line-height:20px;color:var(--muted)}
.f-legal{position:absolute;left:150px;top:232px;font-size:10px;display:flex;gap:14px;color:var(--ink)}
.f-col{position:absolute;top:55px;font-size:10.5px;line-height:21px;color:var(--muted)}
.f-col h4{font-size:14px;font-weight:600;color:var(--ink);margin-bottom:18px;position:relative}
.f-col h4::after{content:"";position:absolute;left:0;bottom:-8px;width:30px;height:2px;background:var(--teal)}
.f-col ul{list-style:none}
.f-col .blue{color:var(--blue)}
.social{display:flex;gap:14px;margin-top:14px}
.social span{width:10px;height:10px;border-radius:50%;background:var(--blue)}
.copy{position:absolute;left:0;width:1200px;top:3880px;height:50px;background:#fff;border-top:1px solid var(--line);text-align:center;font-size:10px;color:var(--muted);line-height:50px}
</style>
</head>
<body>

<header class="site-header">
  <div class="brand"><span class="brand-dot"></span><div><div class="brand-name">Travolex</div><div class="brand-tag">Clever Border Flow</div></div></div>
  <nav class="nav">
    <span class="active">Home</span><span>Products</span><span>Web App</span><span>About Us</span><span>Working at Travolex</span><span>News</span><span>Search Results</span>
  </nav>
  <div class="btn-contact">Contact Us</div>
</header>

<section class="hero">
  <h1>We Are<span>Transforming</span><br>Businesses</h1>
  <p>There are many variations of passages of Lorem Ipsum available, but the majority have suffered alteration in some form, by injected humour, or randomised words which don't look even slightly believable.</p>
  <div class="search"><span>Enter Your Keywords</span><b>SEARCH</b></div>
  <div class="hero-art" role="img" aria-label="Illustration of a team working with a large smartphone showing app screens"></div>
</section>
<div class="notch" style="top:740px;background:#2f8fdc"></div>

<section class="products">
  <div class="sec-head" style="top:75px"><i></i><h2><b>P</b>roducts</h2></div>
  <div class="prod-row">
    <div class="prod"><svg viewBox="0 0 40 40" fill="none" stroke="#fff" stroke-width="2"><rect x="6" y="14" width="18" height="14"/><path d="M24 18h6l4 5v5H24"/><circle cx="12" cy="30" r="3"/><circle cx="29" cy="30" r="3"/></svg>Customs<br>Clearance<br>Processes</div>
    <div class="prod"><svg viewBox="0 0 40 40" fill="none" stroke="#fff" stroke-width="2"><rect x="12" y="12" width="16" height="16" rx="2"/><path d="M16 6v6M24 6v6M16 28v6M24 28v6M6 16h6M6 24h6M28 16h6M28 24h6"/></svg>Artificial<br>Intelligence</div>
    <div class="prod"><svg viewBox="0 0 40 40" fill="none" stroke="#fff" stroke-width="2"><circle cx="20" cy="20" r="6"/><path d="M20 6v5M20 29v5M6 20h5M29 20h5M10 10l4 4M26 26l4 4M30 10l-4 4M14 26l-4 4"/></svg>Process<br>Automation</div>
  </div>
</section>

<section class="about">
  <div class="about-photo" role="img" aria-label="Photo of a man on the phone at a desk with monitors"></div>
  <div class="sec-head"><i></i><h2>About <b>Us</b></h2></div>
  <div class="text">
    <p>With several Pagecraft certified developers, Norvale Digital Ltd is proud to be among the group of Stepwell Pagecraft Partners.</p>
    <p>Having worked on projects for the EU institutions, private banks and insurance ventures we have experience with clients in both the public and private sectors internationally. As a result we have managed to establish a constantly extending track record of satisfied clients who have chosen us as their long term partners, having experienced our high level of professionalism and top notch performance. Further with our solid end to end project lifecycle experience we would be the best resource to help you with consulting, development, training or architecture overview.</p>
  </div>
  <div class="btn-more" style="left:520px;top:330px">Red More &nbsp;›</div>
</section>
<div class="notch" style="top:1560px;background:#3a8fd8"></div>

<section class="webapp">
  <div class="sec-head" style="top:90px"><i></i><h2>Web <b>App</b></h2></div>
  <p class="lead">There are many variations of passages of Lorem Ipsum available, but the majority have suffered alteration in some form.</p>
  <div class="webapp-art"></div>
  <div class="webapp-photo" role="img" aria-label="Photo of hands typing on a laptop keyboard"></div>
  <div class="quote">
    <p>"We needed a Pagecraft development partner who could work alongside our own small project team to bring our new website to life.</p>
    <p>Norvale were the perfect fit for us, able to support us with advice, training and technical expertise. The quality their work was excellent. Marisa and her team were friendly, professional, responsive and full of enthusiasm.</p>
  </div>
  <div class="btn-more" style="left:478px;top:495px">Red More &nbsp;›</div>
  <div class="strip">"Customs clearance processes for forwarding companies by Applying<br>a web application..."<b>Web App</b></div>
</section>

<section class="how">
  <div class="frame"></div>
  <div class="sec-head"><i></i><h2>How <b>it works</b></h2></div>
  <div class="text">
    <p>We needed a Pagecraft development partner who could work alongside our own small project team to bring our new website to life.</p>
    <p>Norvale were the perfect fit for us, able to support us with advice, training and technical expertise. The quality their work was excellent. Marisa and her team</p>
  </div>
  <div class="btn-more" style="left:150px;top:320px;background:linear-gradient(90deg,#1c6fc8,var(--teal))">Red More &nbsp;›</div>
  <div class="video" role="img" aria-label="Video still of a warehouse aisle with stacked boxes"><span class="play"></span></div>
</section>

<section class="news">
  <div class="sec-head" style="top:65px"><i></i><h2><b>N</b>ews</h2></div>
  <div class="cards">
    <article class="card"><div class="ph ph-a" role="img" aria-label="Photo of a developer at a computer"><span class="date">08 MAR 2018</span></div><h3>There are many variations</h3><div class="meta">BY ADMIN &nbsp;|&nbsp; 10 MAY, 2018</div><p>There are many variations of passages of Lorem Ipsum available, but the majority have suffered alteration in some form, by injected humour</p><a>Read More</a></article>
    <article class="card"><div class="ph ph-b" role="img" aria-label="Photo of a team meeting at a wall of notes"><span class="date">08 MAR 2018</span></div><h3>There are many variations</h3><div class="meta">BY ADMIN &nbsp;|&nbsp; 10 MAY, 2018</div><p>There are many variations of passages of Lorem Ipsum available, but the majority have suffered alteration in some form, by injected humour</p><a>Read More</a></article>
    <article class="card"><div class="ph ph-c" role="img" aria-label="Photo of a woman working on a laptop"><span class="date">08 MAR 2018</span></div><h3>There are many variations</h3><div class="meta">BY ADMIN &nbsp;|&nbsp; 10 MAY, 2018</div><p>There are many variations of passages of Lorem Ipsum available, but the majority have suffered alteration in some form, by injected humour</p><a>Read More</a></article>
  </div>
</section>

<section class="map" role="img" aria-label="Map of East and Central Africa with location pins"></section>

<footer class="site-footer">
  <div class="brand"><span class="brand-dot"></span><div><div class="brand-name">Travolex</div><div class="brand-tag">Clever Border Flow</div></div></div>
  <p class="f-about">The following post demonstrates expert tips and tricks, built on Norvale's expertise and day-today use of Pagecraft as well as trainings that we lead for Pagecraft Developers. Constructed in</p>
  <div class="f-legal"><span>Privacy Policy</span><span>Cookie Policy</span><span>Terms and Conditions</span></div>
  <div class="f-col" style="left:492px"><h4>Quick Link</h4><ul><li>Home</li><li>About Us</li><li>What we do</li><li>Our Work</li><li>Blog</li><li>Careers</li><li>Contact Us</li></ul></div>
  <div class="f-col" style="left:672px"><h4>Support</h4><ul><li>Home</li><li>About Us</li><li>What we do</li><li>Our Work</li><li>Blog</li><li>Careers</li><li>Contact Us</li></ul></div>
  <div class="f-col" style="left:842px"><h4>Contact</h4><ul><li>Tel: <span class="blue">+(385) 100-200-300</span></li><li>Email: <span class="blue">hello@norvaledigital.com</span></li></ul>
    <h4 style="margin-top:22px">Connect with us:</h4><div class="social"><span></span><span></span><span></span><span></span></div></div>
</footer>
<div class="copy">© 2018 Web Application. All Rights Reserved.</div>

</body>
</html>
```